Natural Stone Company Redesign

Looking for a fresh, creative, website design. We service Luxury Residential projects in US and Internationally. We would like to see a design that communicates a passion for creative challenging design that is merged with natural stone projects. Our new company Logo is "Inspiration meets Earth"

We like to emphasis from concept to completion, for example, photos of blueprints and/or sketches of a project, then a completion photo of same project.

some websites we like are:
http://www.fernbrockhale.com/
http://lontavimarchitects.com/

We would like to highlight our services of "concept to completion" scenario. Blueprints/sketches to finished products.
Page needed:
Home
About Us
Projects
Contact Us

Target Market(s)

Developers, architects, designers

Industry/Entity Type

It Company

Number of Pages Required

4 page

Font styles to use
Sans Serif

Requirements
Must have
• "Inspiration Meets Earth"
• New, innovative, look.
• Something to grab the attention, and make them think
Nice to have
• Motion on the homepage
• Roll over the finished project photo, and have the name of the stone pop up

```html
<!DOCTYPE html>
<html lang="en">
<head>
<meta charset="utf-8">
<title>Strata Hale — Project</title>
<link rel="stylesheet" href="https://fonts.googleapis.com/css2?family=Open+Sans:wght@400;600;700&display=swap">
<style>
  :root {
    --orange: #fda31f;
    --orange-dark: #e9901a;
    --ink: #3a3a3a;
    --muted: #8a8a8a;
    --star: #b5751a;
    --stat-bg: #f1f1f1;
    --footer: #9d9da0;
    --footer-text: #3d3d40;
    --white: #ffffff;
  }
  * { box-sizing: border-box; margin: 0; padding: 0; }
  html, body { width: 682px; height: 1200px; overflow: hidden; }
  body {
    position: relative;
    background: var(--white);
    font-family: "Open Sans", Arial, sans-serif;
    color: var(--ink);
  }

  /* Header */
  .site-header {
    position: absolute; left: 0; top: 0; width: 682px; height: 45px;
    background: #f6f6f6;
    border-bottom: 1.5px solid var(--orange);
  }
  .brand {
    position: absolute; left: 18px; top: 6px;
    display: flex; align-items: center; gap: 6px;
  }
  .brand-mark { width: 16px; height: 16px; background: var(--orange-dark); }
  .brand-name { font-size: 8.5px; font-weight: 600; letter-spacing: 1.2px; color: var(--ink); }

  .search {
    position: absolute; left: 166px; top: 6px; width: 350px; height: 17px;
    display: flex;
  }
  .search-field {
    flex: 1; background: var(--white); border-radius: 2px 0 0 2px;
    font-size: 6px; color: #b3b3b3; text-align: center; line-height: 17px;
  }
  .search-button {
    width: 38px; background: var(--orange); border-radius: 0 2px 2px 0;
    display: flex; align-items: center; justify-content: center;
  }

  .account {
    position: absolute; left: 571px; top: 6px; width: 93px; height: 17px;
    background: var(--orange); border-radius: 2px;
    display: flex; align-items: center; font-size: 6.5px; color: var(--white);
  }
  .account span { flex: 1; text-align: center; }
  .account .divider { flex: 0 0 1px; height: 11px; background: var(--white); }

  .main-nav {
    position: absolute; top: 28px; left: 0; width: 682px; height: 15px;
    font-size: 6.5px; color: var(--orange);
  }
  .main-nav a { position: absolute; top: 0; line-height: 15px; text-decoration: none; color: inherit; }
  .main-nav .active {
    background: var(--orange); color: var(--white);
    padding: 0 9px; border-radius: 2px 2px 0 0;
  }

  /* Title */
  .page-title {
    position: absolute; top: 88px; left: 0; width: 682px; text-align: center;
    font-size: 39px; font-weight: 700; color: var(--orange); letter-spacing: 0.5px;
  }

  /* Project grid */
  .projects {
    position: absolute; left: 18px; top: 164px;
    display: grid; grid-template-columns: repeat(4, 149px);
    column-gap: 17px; row-gap: 43px;
  }
  .project-card {
    width: 149px; height: 279px;
    box-shadow: 0 1px 2px rgba(0,0,0,0.12);
  }
  .project-photo { height: 193px; }
  .photo-rione { background: linear-gradient(180deg, #4a5a76 0%, #3e4657 45%, #6b4a2e 75%, #27303a 100%); }
  .photo-woodcore { background: linear-gradient(160deg, #a5b8c4 0%, #5a4436 30%, #3d3028 55%, #4f6b80 78%, #2c2a28 100%); }
  .photo-innabale { background: linear-gradient(180deg, #c8d2d6 0%, #b29d6c 25%, #6f7a72 45%, #c7bba6 65%, #5c8a3c 88%, #2f3a2a 100%); }
  .photo-ocean { background: linear-gradient(90deg, #3a2a1a 0%, #c9c0a8 30%, #e8e2d0 50%, #6b8a4a 75%, #2a2418 100%); }

  .project-band {
    height: 65px; background: var(--orange); color: var(--white);
    text-align: center; padding-top: 20px;
  }
  .project-name { font-size: 14px; line-height: 16px; }
  .project-rating { font-size: 8px; letter-spacing: 1px; color: var(--star); margin-top: 1px; }
  .project-rating .off { color: transparent; -webkit-text-stroke: 0.6px var(--star); }

  .project-stats {
    height: 21px; background: var(--stat-bg);
    display: flex; align-items: center; font-size: 7px; color: var(--muted);
  }
  .project-stats .stat { flex: 1; display: flex; justify-content: center; align-items: center; gap: 3px; }
  .project-stats .sep { width: 1px; height: 14px; background: #d2d2d2; }

  /* Footer */
  .site-footer {
    position: absolute; left: 0; top: 1114px; width: 682px; height: 86px;
    background: var(--footer); border-top: 6px solid var(--orange);
  }
  .footer-nav { position: absolute; top: 22px; left: 0; width: 682px; font-size: 6.5px; color: var(--footer-text); }
  .footer-nav a { position: absolute; color: inherit; text-decoration: none; }
  .footer-rule { position: absolute; top: 42px; left: 96px; width: 490px; height: 1px; background: #7d7d80; }
  .social { position: absolute; top: 55px; left: 307px; display: flex; gap: 5px; }
  .social span { width: 9px; height: 9px; border: 1px solid #55555a; border-radius: 2px; }
</style>
</head>
<body>

<header class="site-header">
  <div class="brand">
    <div class="brand-mark"></div>
    <div class="brand-name">STRATA HALE</div>
  </div>
  <div class="search">
    <div class="search-field">Looking for something?</div>
    <div class="search-button">
      <svg width="8" height="8" viewBox="0 0 10 10"><circle cx="4" cy="4" r="3" fill="none" stroke="#fff" stroke-width="1.5"/><line x1="6.2" y1="6.2" x2="9" y2="9" stroke="#fff" stroke-width="1.6"/></svg>
    </div>
  </div>
  <div class="account"><span>Login</span><span class="divider"></span><span>Sign up</span></div>
  <nav class="main-nav">
    <a style="left:250px">Home</a>
    <a class="active" style="left:294px">Project</a>
    <a style="left:355px">About Us</a>
    <a style="left:408px">Contact Us</a>
  </nav>
</header>

<h1 class="page-title">PROJECT</h1>

<svg width="0" height="0" style="position:absolute">
  <defs>
    <symbol id="icon-heart" viewBox="0 0 10 9"><path d="M5 9 L1 5 A2.4 2.4 0 0 1 5 1.6 A2.4 2.4 0 0 1 9 5 Z" fill="#8a8a8a"/></symbol>
    <symbol id="icon-comment" viewBox="0 0 11 9"><ellipse cx="6" cy="3.6" rx="4.8" ry="3.4" fill="#8a8a8a"/><path d="M2.5 5.5 L1 8.5 L5 6.6 Z" fill="#8a8a8a"/></symbol>
  </defs>
</svg>

<main class="projects">
  <!-- row 1 -->
  <article class="project-card">
    <div class="project-photo photo-rione" role="img" aria-label="Tropical villa at dusk with palm trees and a reflecting pool"></div>
    <div class="project-band"><div class="project-name">Rione Resident</div><div class="project-rating">★★★<span class="off">★★</span></div></div>
    <div class="project-stats"><div class="stat"><svg width="8" height="7"><use href="#icon-heart"/></svg>122</div><div class="sep"></div><div class="stat"><svg width="9" height="7"><use href="#icon-comment"/></svg>32</div></div>
  </article>
  <article class="project-card">
    <div class="project-photo photo-woodcore" role="img" aria-label="Carved stone bathtub beside a lava rock wall and tropical leaves"></div>
    <div class="project-band"><div class="project-name">Woodcore Resident</div><div class="project-rating">★★★★<span class="off">★</span></div></div>
    <div class="project-stats"><div class="stat"><svg width="8" height="7"><use href="#icon-heart"/></svg>126</div><div class="sep"></div><div class="stat"><svg width="9" height="7"><use href="#icon-comment"/></svg>12</div></div>
  </article>
  <article class="project-card">
    <div class="project-photo photo-innabale" role="img" aria-label="Curved stone-edged pool on a coastal terrace"></div>
    <div class="project-band"><div class="project-name">Innabale Resident</div><div class="project-rating">★★★★★</div></div>
    <div class="project-stats"><div class="stat"><svg width="8" height="7"><use href="#icon-heart"/></svg>212</div><div class="sep"></div><div class="stat"><svg width="9" height="7"><use href="#icon-comment"/></svg>35</div></div>
  </article>
  <article class="project-card">
    <div class="project-photo photo-ocean" role="img" aria-label="Open glass doors onto a bright stone-floored living space"></div>
    <div class="project-band"><div class="project-name">Ocean Scape Resident</div><div class="project-rating">★★★<span class="off">★★</span></div></div>
    <div class="project-stats"><div class="stat"><svg width="8" height="7"><use href="#icon-heart"/></svg>120</div><div class="sep"></div><div class="stat"><svg width="9" height="7"><use href="#icon-comment"/></svg>112</div></div>
  </article>

  <!-- row 2 -->
  <article class="project-card">
    <div class="project-photo photo-rione" role="img" aria-label="Tropical villa at dusk with palm trees and a reflecting pool"></div>
    <div class="project-band"><div class="project-name">Rione Resident</div><div class="project-rating">★★★<span class="off">★★</span></div></div>
    <div class="project-stats"><div class="stat"><svg width="8" height="7"><use href="#icon-heart"/></svg>122</div><div class="sep"></div><div class="stat"><svg width="9" height="7"><use href="#icon-comment"/></svg>32</div></div>
  </article>
  <article class="project-card">
    <div class="project-photo photo-woodcore" role="img" aria-label="Carved stone bathtub beside a lava rock wall and tropical leaves"></div>
    <div class="project-band"><div class="project-name">Woodcore Resident</div><div class="project-rating">★★★★<span class="off">★</span></div></div>
    <div class="project-stats"><div class="stat"><svg width="8" height="7"><use href="#icon-heart"/></svg>126</div><div class="sep"></div><div class="stat"><svg width="9" height="7"><use href="#icon-comment"/></svg>12</div></div>
  </article>
  <article class="project-card">
    <div class="project-photo photo-innabale" role="img" aria-label="Curved stone-edged pool on a coastal terrace"></div>
    <div class="project-band"><div class="project-name">Innabale Resident</div><div class="project-rating">★★★★★</div></div>
    <div class="project-stats"><div class="stat"><svg width="8" height="7"><use href="#icon-heart"/></svg>212</div><div class="sep"></div><div class="stat"><svg width="9" height="7"><use href="#icon-comment"/></svg>35</div></div>
  </article>
  <article class="project-card">
    <div class="project-photo photo-ocean" role="img" aria-label="Open glass doors onto a bright stone-floored living space"></div>
    <div class="project-band"><div class="project-name">Ocean Scape Resident</div><div class="project-rating">★★★<span class="off">★★</span></div></div>
    <div class="project-stats"><div class="stat"><svg width="8" height="7"><use href="#icon-heart"/></svg>120</div><div class="sep"></div><div class="stat"><svg width="9" height="7"><use href="#icon-comment"/></svg>112</div></div>
  </article>

  <!-- row 3 -->
  <article class="project-card">
    <div class="project-photo photo-rione" role="img" aria-label="Tropical villa at dusk with palm trees and a reflecting pool"></div>
    <div class="project-band"><div class="project-name">Rione Resident</div><div class="project-rating">★★★<span class="off">★★</span></div></div>
    <div class="project-stats"><div class="stat"><svg width="8" height="7"><use href="#icon-heart"/></svg>122</div><div class="sep"></div><div class="stat"><svg width="9" height="7"><use href="#icon-comment"/></svg>32</div></div>
  </article>
  <article class="project-card">
    <div class="project-photo photo-woodcore" role="img" aria-label="Carved stone bathtub beside a lava rock wall and tropical leaves"></div>
    <div class="project-band"><div class="project-name">Woodcore Resident</div><div class="project-rating">★★★★<span class="off">★</span></div></div>
    <div class="project-stats"><div class="stat"><svg width="8" height="7"><use href="#icon-heart"/></svg>126</div><div class="sep"></div><div class="stat"><svg width="9" height="7"><use href="#icon-comment"/></svg>12</div></div>
  </article>
  <article class="project-card">
    <div class="project-photo photo-innabale" role="img" aria-label="Curved stone-edged pool on a coastal terrace"></div>
    <div class="project-band"><div class="project-name">Innabale Resident</div><div class="project-rating">★★★★★</div></div>
    <div class="project-stats"><div class="stat"><svg width="8" height="7"><use href="#icon-heart"/></svg>212</div><div class="sep"></div><div class="stat"><svg width="9" height="7"><use href="#icon-comment"/></svg>35</div></div>
  </article>
  <article class="project-card">
    <div class="project-photo photo-ocean" role="img" aria-label="Open glass doors onto a bright stone-floored living space"></div>
    <div class="project-band"><div class="project-name">Ocean Scape Resident</div><div class="project-rating">★★★<span class="off">★★</span></div></div>
    <div class="project-stats"><div class="stat"><svg width="8" height="7"><use href="#icon-heart"/></svg>120</div><div class="sep"></div><div class="stat"><svg width="9" height="7"><use href="#icon-comment"/></svg>112</div></div>
  </article>
</main>

<footer class="site-footer">
  <nav class="footer-nav">
    <a style="left:245px">Home</a>
    <a style="left:299px">Project</a>
    <a style="left:351px">Abous Us</a>
    <a style="left:404px">Contact Us</a>
  </nav>
  <div class="footer-rule"></div>
  <div class="social" aria-label="Social links">
    <span></span><span></span><span></span><span></span><span></span>
  </div>
</footer>

</body>
</html>
```